Email template wanted for a baby/toddler's daily diary

We have an early years EdTech app for childminders, nannies and nursery/kindergarten staff which captures a child's day and then sends an email in the form of a daily dairy to the parents.
At the moment the format for this daily diary is awful and could be greatly improved on to look more appealing to the parent - please see attached file.

We would like an email html template which contains the same headings but looks much more appealing to the parent using appropriate colour scheme, images and icons to represent the various section. It could look more diary like.

Target Market(s)

Parents of babies/young children

Industry/Entity Type

Baby

Font styles to use
Script

Requirements
Must have
• All the sections contained in the attached file.
• Please also take a look at our website: www.hollowfinch.co.uk to get a feel for colour schemes if that helps

```html
<!DOCTYPE html>
<html lang="en">
<head>
<meta charset="utf-8">
<title>Oliver's Day at Little Wrens</title>
<link rel="stylesheet" href="https://fonts.googleapis.com/css2?family=Open+Sans:wght@400;600;700&family=Roboto+Condensed:wght@700&display=swap">
<style>
  :root{
    --brand:#c0522e;
    --brand-dark:#a9452a;
    --ink:#4a3a33;
    --ink-soft:#6b5a52;
    --paper:#ffffff;
    --icon:#b54f2f;
    --footer-text:#f6ddd2;
  }
  *{box-sizing:border-box;margin:0;padding:0}
  html,body{width:851px;height:1200px;overflow:hidden;background:var(--paper)}
  body{font-family:"Open Sans",Arial,sans-serif;color:var(--ink);position:relative}

  .hero{position:absolute;left:0;top:0;width:851px;height:372px;
    background:linear-gradient(90deg,#2f5a4e 0%,#5d7d6f 22%,#c9a48a 45%,#e8d3c2 60%,#d9b8a0 78%,#f1e5da 100%)}
  .brand-bar{position:absolute;left:0;top:0;width:851px;height:62px;background:var(--brand);opacity:.95;
    display:flex;align-items:center;padding-left:24px}
  .brand-name{font-family:"Open Sans",Arial,sans-serif;font-weight:700;font-size:30px;color:#fff;letter-spacing:-.5px}

  .greeting{position:absolute;left:80px;top:390px;font-size:22px;color:var(--brand)}
  .title{position:absolute;left:80px;top:440px;font-family:"Roboto Condensed",Arial,sans-serif;
    font-size:33px;color:var(--ink);letter-spacing:.5px}

  .entry{position:absolute;display:flex;gap:18px;align-items:flex-start}
  .entry svg{flex:none}
  .entry h3{font-size:17px;font-weight:700;color:var(--ink);margin-bottom:4px}
  .entry p{font-size:16px;color:var(--ink-soft);line-height:1.35}
  .meals dt{font-size:17px;font-weight:700;color:var(--ink);margin-top:14px}
  .meals dt:first-child{margin-top:0}
  .meals dd{font-size:16px;color:var(--ink-soft);margin-top:4px}

  .footer{position:absolute;left:0;top:1058px;width:851px;height:142px;background:var(--brand-dark);
    display:grid;grid-template-columns:repeat(4,1fr);padding:12px 40px 0 58px;gap:14px}
  .footer h4{font-size:12px;font-weight:600;color:#fff;margin-bottom:6px;padding-bottom:4px;border-bottom:1px solid rgba(255,255,255,.35)}
  .footer li{list-style:none;font-size:9.5px;line-height:11.5px;color:var(--footer-text)}
</style>
</head>
<body>
  <header class="hero" role="img" aria-label="Photo strip of children learning at a chalkboard and drawing with a smiling carer">
    <div class="brand-bar"><span class="brand-name">Hollowfinch</span></div>
  </header>

  <p class="greeting">Dear Clara,</p>
  <h1 class="title">OLIVER'S DAY AT LITTLE WRENS</h1>

  <section class="entry" style="left:80px;top:530px">
    <svg width="62" height="62" viewBox="0 0 62 62" aria-hidden="true">
      <path d="M31 6a25 25 0 1 1-24 18" fill="none" stroke="var(--icon)" stroke-width="4" stroke-linecap="round"/>
      <path d="M3 18l4 7 7-4" fill="none" stroke="var(--icon)" stroke-width="4" stroke-linecap="round" stroke-linejoin="round"/>
      <text x="31" y="39" text-anchor="middle" font-family="Roboto Condensed,Arial,sans-serif" font-weight="700" font-size="20" fill="var(--icon)">24</text>
    </svg>
    <div><h3>What I've done today</h3><p>humm lost this</p></div>
  </section>

  <section class="entry" style="left:80px;top:690px">
    <svg width="62" height="62" viewBox="0 0 62 62" aria-hidden="true">
      <circle cx="31" cy="31" r="29" fill="var(--icon)"/>
      <circle cx="31" cy="31" r="13" fill="none" stroke="#fff" stroke-width="3"/>
      <path d="M12 16v10M9 16v8q0 4 3 4t3-4v-8M12 28v20M50 16q-5 4-5 14h5v18" fill="none" stroke="#fff" stroke-width="2.5" stroke-linecap="round"/>
    </svg>
    <div><h3>Food</h3><p>Oliver did not eat anything today</p></div>
  </section>

  <section class="entry" style="left:80px;top:800px">
    <svg width="62" height="62" viewBox="0 0 62 62" aria-hidden="true">
      <circle cx="31" cy="31" r="29" fill="var(--icon)"/>
      <rect x="19" y="13" width="12" height="16" rx="2" fill="#fff"/>
      <path d="M17 30h30q0 12-12 13l2 7H25l2-7q-10-2-10-13z" fill="#fff"/>
    </svg>
    <div><h3>Toilet</h3><p>Oliver had 2 nappy changes<br>today and 3 poo(s).</p></div>
  </section>

  <section class="entry" style="left:80px;top:955px">
    <svg width="62" height="62" viewBox="0 0 62 62" aria-hidden="true">
      <rect x="0" y="0" width="62" height="62" rx="6" fill="var(--icon)"/>
      <path d="M28 8h6v5h-6z M25 14h12v4H25z M24 19h14v33q0 3-3 3h-8q-3 0-3-3z" fill="#fff"/>
      <path d="M27 28h5M27 35h5M27 42h5" stroke="var(--icon)" stroke-width="2"/>
    </svg>
    <div><h3>Baby Bottles</h3><p>Oliver has 3 milk bottle(s) today</p></div>
  </section>

  <section class="entry" style="left:425px;top:530px">
    <svg width="62" height="62" viewBox="0 0 62 62" aria-hidden="true">
      <rect x="0" y="10" width="62" height="42" rx="6" fill="var(--icon)"/>
      <rect x="8" y="22" width="12" height="9" rx="3" fill="#fff"/>
      <path d="M23 22h26q5 0 5 5v4H23z M6 34h50v6H6z" fill="#fff"/>
    </svg>
    <div><h3>Sleep</h3><p>Oliver slept from<br>15:20 to 15:27 today</p></div>
  </section>

  <section class="entry" style="left:425px;top:690px">
    <svg width="62" height="62" viewBox="0 0 62 62" aria-hidden="true">
      <circle cx="31" cy="31" r="29" fill="var(--icon)"/>
      <circle cx="31" cy="31" r="13" fill="none" stroke="#fff" stroke-width="3"/>
      <path d="M12 16v10M9 16v8q0 4 3 4t3-4v-8M12 28v20M50 16q-5 4-5 14h5v18" fill="none" stroke="#fff" stroke-width="2.5" stroke-linecap="round"/>
    </svg>
    <dl class="meals">
      <dt>Breakfast</dt><dd>Cereal</dd>
      <dt>Morning Snack</dt><dd>Banana</dd>
      <dt>Lunch</dt><dd>Baked Potato with Cheese</dd>
      <dt>Afternoon Snack</dt><dd>Pear</dd>
    </dl>
  </section>

  <footer class="footer">
    <nav><h4>Childcare Practitioners</h4><ul>
      <li>Features &amp; Benefits</li><li>Pricing</li><li>Reviews &amp; Testimonials</li><li>Register for Free Trial</li><li>Sign In</li><li>T&amp;Cs for Childcare Practitioners</li><li>Privacy &amp; Cookie Policy</li></ul></nav>
    <nav><h4>Parents &amp; Guardians</h4><ul>
      <li>Parents' Guide</li><li>Terms and Conditions for Parents</li><li>Privacy &amp; Cookie Policy</li></ul></nav>
    <nav><h4>Help &amp; Resources</h4><ul>
      <li>Frequently Asked Questions</li><li>Videos &amp; Guides</li><li>Early Years Pupil Premium Tool</li><li>Security</li><li>Site Map</li><li>Support</li></ul></nav>
    <nav><h4>Contact &amp; Information</h4><ul>
      <li>About Us</li><li>Our Team</li><li>Our Advisors</li><li>News &amp; Media</li><li>Blog</li><li>Contact Us</li><li>Newsletter</li><li>Job Opportunities</li><li>Hollowfinch Foundation</li></ul></nav>
  </footer>
</body>
</html>
```